Plastic Surgeon Stationary Design

I Already have the logo. I Want and a clean, minimalist and elegant project. Please, I prefer Black, White and Gold color but you're free to try another ones. Business card,
Letterhead (A4 and Office), Recipes (Letter Pad) (A5), Envelop, Invoice, Computer Bill, Bill Book, Single A4 page size,
You Have to create at least the same materials I already own. I would like to a file to use in word to print letterheads and letter pad.
What I want that you make more changes are the envelopes that are to colorful and not elegant.
I'll not accept any design without my addresses as you can guide yourself with the models I provide.
Here are the addresses too:
"www.rubemtavorasilva.example" (website)
(My clinics' address)
"SÃO PAULO
Rua Lucas Bentim, 3180, Lucas Bentim Office, Cj 204
São Paulo - SP
(11) 90123-4567"
"BALNEÁRIO CAMBORIÚ
Rua Clemente Vilaça, 418, 7° andar
Edificio Torre Quaresma
Balneário Camboriú - SC
(047) 9012-3456"
Attention: Letterheads, Recipes, have to contain "CRM/SC 52.807 and CRM/SP 308.614" close to my name (Dr. Rubem Távora - Cirurgião Plástico), it is usually placed at the bottom.
Designers, attention!
During the process of creating bear in mind that the details of the logo, as the faces on the sides, are designed to be subtle. Highlight other such details affect the delicacy and elegance of the logo and visual identity.
When you are creating stationery, do not abuse the use of the logo, it should be used once or at most two times in each item.
Remember! Each stationery set must submit 3 models, one with the address "Balneario Camboriu", another with the address of "São Paulo" and the third containing both addresses.
The model letter envelope, folder type bag for letterhead and folder with inner pocket that provided a model did not please me because they are very flashy. Give preference to the use of white or black background.
PLEASE! Seek inspiration in the models contained in this link:
https://www.filecrate.example/sh/kq27zp41wcx905m/PlRtVuY_QX
In this link you can find my PAST Stationary Itens, so it can help you on your work
https://docuvault.example/7ZK3NB8QeT2LwYhR
Reason: Nobody presented anything useful.
Reason: still waiting some designers send their projects
Reason: Still Waiting Some Designs....
Target Market(s)
Mostly females with good economical condition. (Class A and AB)
Industry/Entity Type
Business
Requirements
Must have
- You have to provide 3 models of each paper, one with the address of São Paulo, another with the Balneario Camboriú address, and the third one with both addresses.

```html
<!DOCTYPE html>
<html lang="pt">
<head>
<meta charset="utf-8">
<title>Rubem Távora — Cirurgia Plástica · Stationery</title>
<link rel="stylesheet" href="https://fonts.googleapis.com/css2?family=Libre+Baskerville:wght@700&family=Josefin+Sans:wght@400;600&family=Open+Sans:wght@400;600&display=swap">
<style>
:root{
  --bg:#efefef;
  --paper:#f7f7f6;
  --ink:#2a2a2a;
  --ink-soft:#3a3a3a;
  --gold:#b39a5d;
  --gold-light:#c4ab6c;
  --text:#333;
}
*{margin:0;padding:0;box-sizing:border-box}
html,body{width:1200px;height:869px;overflow:hidden;background:var(--bg)}
.canvas{position:relative;width:1200px;height:869px;font-family:"Open Sans",sans-serif;color:var(--text)}
.piece{position:absolute;overflow:hidden;box-shadow:0 2px 6px rgba(0,0,0,.18)}
.brand{position:absolute;text-align:center;transform:translateX(-50%)}
.brand-dot{display:block;margin:0 auto;border-radius:50%;background:var(--gold)}
.brand-name{display:block;font-family:"Libre Baskerville",serif;font-weight:700;letter-spacing:-.02em;white-space:nowrap;line-height:1.1}
.brand-tag{display:block;font-family:"Josefin Sans",sans-serif;letter-spacing:.3em;white-space:nowrap;color:var(--gold)}
.label{font-family:"Josefin Sans",sans-serif;font-weight:600;color:var(--gold);text-transform:uppercase}
.addr{font-family:"Josefin Sans",sans-serif;line-height:1.25}
.url{font-family:"Josefin Sans",sans-serif;color:var(--gold);letter-spacing:.15em;position:absolute;white-space:nowrap}
.gold-band{position:absolute;left:0;right:0;background:var(--gold)}

/* Letterhead */
.letterhead{left:201px;top:54px;width:365px;height:518px;background:var(--paper)}
.letterhead .brand{left:182px;top:20px}
.letterhead .brand-dot{width:18px;height:18px;margin-bottom:6px}
.letterhead .brand-name{font-size:14px;color:var(--ink)}
.letterhead .brand-tag{font-size:5px;margin-top:3px;color:var(--ink)}
.letterhead .crm{display:block;font-size:4.5px;margin-top:4px;color:#555}
.letter-date{position:absolute;left:45px;top:142px;font-size:6.5px;font-weight:600;color:var(--ink)}
.letter-subject{position:absolute;left:45px;top:156px;font-family:"Josefin Sans",sans-serif;font-weight:600;font-size:9px;letter-spacing:.12em;color:var(--gold)}
.letter-body{position:absolute;left:45px;top:182px;width:276px;font-size:5.3px;font-weight:600;line-height:1.9;color:#444}
.letter-body p{margin-bottom:8px}
.letter-footer{position:absolute;left:0;right:0;bottom:0;height:50px;background:var(--ink);border-top:2px solid var(--gold)}
.letter-footer .col{position:absolute;top:8px;font-size:4.6px;color:#ddd}
.letter-footer .label{font-size:4.6px}
.letter-footer .url{right:26px;top:4px;font-size:3.8px}

/* Folder */
.folder{left:630px;top:30px;width:431px;height:544px;background:var(--ink)}
.folder-photo{position:absolute;inset:0;background:linear-gradient(160deg,#4a4a4a 0%,#333 45%,#2b2b2b 70%,#3b3b3b 100%)}
.folder .brand{left:215px;top:170px}
.folder .brand-dot{width:32px;height:32px;margin-bottom:12px}
.folder .brand-name{font-size:25px;color:var(--gold)}
.folder .brand-tag{font-size:9px;margin-top:6px}
.folder .url{left:0;right:0;text-align:center;top:356px;font-size:10px}
.folder .gold-band{bottom:0;height:13px}

/* Business cards */
.card-front{left:69px;top:617px;width:165px;height:68px;background:var(--paper)}
.card-front .brand{left:82px;top:6px}
.card-front .brand-dot{width:9px;height:9px;margin-bottom:3px}
.card-front .brand-name{font-size:8px;color:var(--ink)}
.card-front .brand-tag{font-size:3px;margin-top:1px;color:var(--ink)}
.card-rule{position:absolute;left:9px;right:9px;top:50px;border-top:1px solid #bbb}
.card-front .col{position:absolute;top:52px;font-size:3.2px;color:#444}
.card-front .label{font-size:3.2px}
.card-front .gold-band{bottom:0;height:2px}
.card-back{left:69px;top:737px;width:165px;height:94px;background:var(--ink)}
.card-back .url{left:0;right:0;text-align:center;top:28px;font-size:4.5px}

/* Envelopes */
.envelope-front{left:277px;top:631px;width:409px;height:193px;background:var(--ink)}
.envelope-front .brand{left:81px;top:24px}
.envelope-front .brand-dot{width:18px;height:18px;margin-bottom:8px}
.envelope-front .brand-name{font-size:15px;color:var(--gold)}
.envelope-front .brand-tag{font-size:5.5px;margin-top:3px}
.envelope-front .url{right:27px;top:116px;font-size:6px}
.envelope-front .gold-band{bottom:0;height:7px}
.envelope-back{left:726px;top:631px;width:409px;height:193px;background:var(--gold)}
.envelope-flap{position:absolute;left:0;top:0;width:409px;height:82px}
.envelope-back .brand{left:204px;top:20px}
.envelope-back .brand-dot{width:20px;height:20px}
.envelope-back .address-block{position:absolute;left:0;right:0;top:92px;text-align:center;font-size:6.5px;color:var(--ink)}
.envelope-back .label{color:var(--ink);font-size:6.5px}
</style>
</head>
<body>
<main class="canvas">

  <section class="piece letterhead" aria-label="Letterhead">
    <div class="brand">
      <span class="brand-dot"></span>
      <span class="brand-name">Rubem Távora</span>
      <span class="brand-tag">CIRURGIA PLÁSTICA</span>
      <span class="crm">CRM/SC 52.807 and CRM/SP 308.614</span>
    </div>
    <p class="letter-date">16 . September . 2013</p>
    <p class="letter-subject">SUBJECT:</p>
    <div class="letter-body">
      <p>Lorem ipsum dolor sit amet, consectetur adipisicing elit, sed do eiusmod tempor incididunt ut labore et dolore magna aliqua. Ut enim ad minim veniam, quis nostrud exercitation ullamco laboris nisi ut aliquip ex ea commodo consequat. Duis aute irure dolor in reprehenderit in voluptate velit esse cillum dolore eu fugiat nulla pariatur. Excepteur sint occaecat cupidatat non proident, sunt in culpa qui officia deserunt mollit anim id est laborum.</p>
      <p>Sed ut perspiciatis unde omnis iste natus error sit voluptatem accusantium doloremque laudantium, totam rem aperiam, eaque ipsa quae ab illo inventore veritatis et quasi architecto beatae vitae dicta sunt explicabo. Nemo enim ipsam voluptatem quia voluptas sit aspernatur aut odit aut fugit, sed quia consequuntur magni dolores eos qui ratione voluptatem sequi nesciunt. Neque porro quisquam est, qui dolorem ipsum quia dolor sit amet, consectetur, adipisci velit, sed quia non numquam eius modi tempora incidunt ut labore et dolore magnam aliquam quaerat voluptatem. Ut enim ad minima veniam, quis nostrum exercitationem ullam corporis suscipit laboriosam, nisi ut aliquid ex ea commodi consequatur.</p>
      <p>Quis autem vel eum iure reprehenderit qui in ea voluptate velit esse quam nihil molestiae consequatur, vel illum qui dolorem eum fugiat quo voluptas nulla pariatur</p>
    </div>
    <footer class="letter-footer">
      <div class="col addr" style="left:29px">
        <span class="label">São Paulo</span><br>
        Rua Lucas Bentim, 3180,<br>Lucas Bentim Office, Cj 204<br>São Paulo - SP<br>(11) 90123-4567
      </div>
      <div class="col addr" style="left:118px">
        <span class="label">Balneário Camboriú</span><br>
        Rua Clemente Vilaça, 418, 7° andar<br>Edificio Torre Quaresma<br>Balneário Camboriú - SC<br>(047) 9012-3456
      </div>
      <span class="url">www.rubemtavorasilva.example</span>
    </footer>
  </section>

  <section class="piece folder" aria-label="Presentation folder">
    <div class="folder-photo" role="img" aria-label="Dark monochrome close-up portrait photograph filling the folder cover"></div>
    <div class="brand">
      <span class="brand-dot"></span>
      <span class="brand-name">Rubem Távora</span>
      <span class="brand-tag">CIRURGIA PLÁSTICA</span>
    </div>
    <span class="url">www.rubemtavorasilva.example</span>
    <div class="gold-band"></div>
  </section>

  <section class="piece card-front" aria-label="Business card front">
    <div class="brand">
      <span class="brand-dot"></span>
      <span class="brand-name">Rubem Távora</span>
      <span class="brand-tag">CIRURGIA PLÁSTICA</span>
    </div>
    <div class="card-rule"></div>
    <div class="col addr" style="left:9px">
      <span class="label">São Paulo</span><br>Rua Lucas Bentim, 3180,<br>Lucas Bentim Office, Cj 204<br>São Paulo - SP<br>(11) 90123-4567
    </div>
    <div class="col addr" style="right:9px;text-align:right">
      <span class="label">Balneário Camboriú</span><br>Rua Clemente Vilaça, 418, 7° andar<br>Edificio Torre Quaresma<br>Balneário Camboriú - SC<br>(047) 9012-3456
    </div>
    <div class="gold-band"></div>
  </section>

  <section class="piece card-back" aria-label="Business card back">
    <span class="url">www.rubemtavorasilva.example</span>
  </section>

  <section class="piece envelope-front" aria-label="Envelope front">
    <div class="brand">
      <span class="brand-dot"></span>
      <span class="brand-name">Rubem Távora</span>
      <span class="brand-tag">CIRURGIA PLÁSTICA</span>
    </div>
    <span class="url">www.rubemtavorasilva.example</span>
    <div class="gold-band"></div>
  </section>

  <section class="piece envelope-back" aria-label="Envelope back">
    <svg class="envelope-flap" viewBox="0 0 409 82" aria-hidden="true">
      <path d="M0 0H409V6L390 78H19L0 6Z" fill="var(--ink)"/>
    </svg>
    <div class="brand"><span class="brand-dot"></span></div>
    <div class="address-block addr">
      <span class="label">São Paulo</span><br>Rua Lucas Bentim, 3180,<br>Lucas Bentim Office, Cj 204<br>São Paulo - SP<br>(11) 90123-4567
    </div>
  </section>

</main>
</body>
</html>
```